skin care company
Project: skin care company
skin care company - Personal Care
Creative Brief
Simple
Carla Menzoli
General Manager
Orlen Business Plaza 14th Floor Marvel Hadi Street Dubai, UAE
cmenzoli@lurecoskin.com
For letter head please use info@lurecoskin.com
bghamdi bghamdi
for b.card both sides need to be black. also add this salgon under the logo in b.card Where Skin Meets Nature
letterhead sample attached.
Attached.
RAS518 RAS518
hi bghamdi did you not attach your logo?
For business card. Contact information on side and logo in back side.
B.card: add icon for mobile and for work phone. letterhead: in the footer put public email info@lurecoskin.com work phone: +97143918426 and address in one line. also there is missing stationary such as envelop.

```html
<!DOCTYPE html>
<html lang="en">
<head>
<meta charset="utf-8">
<title>Lureco Stationery</title>
<link rel="stylesheet" href="https://fonts.googleapis.com/css2?family=Montserrat:wght@300;400;600&display=swap">
<style>
  :root {
    --backdrop: #a2a2a2;
    --paper: #ffffff;
    --charcoal: #3b3b3b;
    --leaf: #7dc22a;
    --ink: #3a3a3a;
    --mist: #d6d6d6;
    --soft-white: #f2f2f2;
  }
  * { margin: 0; padding: 0; box-sizing: border-box; }
  html, body { width: 1200px; height: 799px; overflow: hidden; }
  body {
    background: var(--backdrop);
    font-family: "Montserrat", Arial, sans-serif;
    position: relative;
  }
  .brand-name {
    position: absolute;
    font-weight: 300;
    letter-spacing: 0.12em;
    line-height: 1;
    white-space: nowrap;
  }

  /* Letterhead */
  .letterhead {
    position: absolute; left: 34px; top: 31px;
    width: 499px; height: 737px;
    background: var(--paper);
    overflow: hidden;
  }
  .letterhead .brand-name { left: 268px; top: 80px; font-size: 27px; color: var(--leaf); }
  .letterhead-footer {
    position: absolute; left: 0; top: 662px; width: 100%;
    font-size: 8px; color: var(--ink); line-height: 1.35;
  }
  .footer-item { position: absolute; display: flex; gap: 6px; align-items: flex-start; }
  .footer-item svg { width: 9px; height: 9px; flex: none; margin-top: 1px; }
  .footer-phone { left: 45px; }
  .footer-email { left: 168px; }
  .footer-address { left: 362px; }
  .footer-address span { font-size: 6px; }
  .corner-stripe { position: absolute; left: 0; bottom: 0; }

  /* Business card — contact side */
  .card-contact {
    position: absolute; left: 566px; top: 31px;
    width: 600px; height: 353px;
    background: var(--charcoal);
    overflow: hidden;
  }
  .card-contact .brand-name { left: 62px; top: 62px; font-size: 34px; color: var(--leaf); }
  .holder-name {
    position: absolute; left: 62px; top: 152px;
    font-size: 16px; font-weight: 600; letter-spacing: 0.08em;
    color: var(--soft-white);
  }
  .holder-title {
    position: absolute; left: 92px; top: 174px;
    font-size: 7px; letter-spacing: 0.22em; color: #bdbdbd;
  }
  .contact-list { position: absolute; left: 62px; top: 202px; list-style: none; color: var(--soft-white); font-size: 10px; line-height: 1.3; }
  .contact-list li { display: flex; gap: 9px; align-items: flex-start; margin-bottom: 7px; }
  .contact-list svg { width: 11px; height: 11px; flex: none; margin-top: 1px; }
  .contact-list .address { font-size: 7px; line-height: 1.35; }

  /* Business card — logo side */
  .card-logo {
    position: absolute; left: 566px; top: 415px;
    width: 600px; height: 353px;
    background: var(--leaf);
  }
  .card-logo .brand-name {
    left: 0; right: 0; top: 140px; text-align: center;
    font-size: 68px; color: var(--paper); letter-spacing: 0.14em;
  }
</style>
</head>
<body>

<section class="letterhead" aria-label="Letterhead">
  <span class="brand-name">LURECO</span>

  <footer class="letterhead-footer">
    <div class="footer-item footer-phone">
      <svg viewBox="0 0 10 10"><circle cx="5" cy="5" r="5" fill="#3a3a3a"/><path d="M3.3 2.6l1 1-.6.7a4 4 0 0 0 2 2l.7-.6 1 1-.7.8c-2 0-4-2-4-4z" fill="#fff"/></svg>
      <span>+97143918426<br>+971506148735</span>
    </div>
    <div class="footer-item footer-email">
      <svg viewBox="0 0 10 10"><rect x="0.5" y="2" width="9" height="6.4" fill="#3a3a3a"/><path d="M0.8 2.4L5 5.6l4.2-3.2" stroke="#fff" stroke-width="0.8" fill="none"/></svg>
      <span>info@lurecoskin.com</span>
    </div>
    <div class="footer-item footer-address">
      <svg viewBox="0 0 10 10"><path d="M5 0.3a3.4 3.4 0 0 1 3.4 3.4C8.4 6.2 5 9.7 5 9.7S1.6 6.2 1.6 3.7A3.4 3.4 0 0 1 5 .3z" fill="#3a3a3a"/><circle cx="5" cy="3.7" r="1.2" fill="#fff"/></svg>
      <span>Verrand Business Plaza<br>14th Floor<br>Marvel Hadi Street<br>Dubai, UAE</span>
    </div>
  </footer>

  <svg class="corner-stripe" width="499" height="14" viewBox="0 0 499 14" aria-hidden="true">
    <polygon points="300,0 499,0 499,14 312,14" fill="#d6d6d6"/>
    <polygon points="392,0 499,0 499,14 404,14" fill="#7dc22a"/>
  </svg>
</section>

<section class="card-contact" aria-label="Business card, contact side">
  <span class="brand-name">LURECO</span>
  <h1 class="holder-name">CARLA MENZOLI</h1>
  <p class="holder-title">GENERAL MANAGER</p>

  <ul class="contact-list">
    <li>
      <svg viewBox="0 0 10 10"><circle cx="5" cy="5" r="5" fill="#f2f2f2"/><path d="M3.3 2.6l1 1-.6.7a4 4 0 0 0 2 2l.7-.6 1 1-.7.8c-2 0-4-2-4-4z" fill="#3b3b3b"/></svg>
      <span>+97143918426<br>+971506148735</span>
    </li>
    <li>
      <svg viewBox="0 0 10 10"><rect x="0.5" y="2" width="9" height="6.4" fill="#f2f2f2"/><path d="M0.8 2.4L5 5.6l4.2-3.2" stroke="#3b3b3b" stroke-width="0.8" fill="none"/></svg>
      <span>cmenzoli@lurecoskin.com</span>
    </li>
    <li>
      <svg viewBox="0 0 10 10"><path d="M5 0.3a3.4 3.4 0 0 1 3.4 3.4C8.4 6.2 5 9.7 5 9.7S1.6 6.2 1.6 3.7A3.4 3.4 0 0 1 5 .3z" fill="#f2f2f2"/><circle cx="5" cy="3.7" r="1.2" fill="#3b3b3b"/></svg>
      <span class="address">Verrand Business Plaza<br>14th Floor<br>Marvel Hadi Street<br>Dubai, UAE</span>
    </li>
  </ul>

  <svg class="corner-stripe" width="600" height="12" viewBox="0 0 600 12" aria-hidden="true">
    <polygon points="405,0 600,0 600,12 418,12" fill="#d6d6d6"/>
    <polygon points="425,0 600,0 600,12 438,12" fill="#7dc22a"/>
  </svg>
</section>

<section class="card-logo" aria-label="Business card, logo side">
  <span class="brand-name">LURECO</span>
</section>

</body>
</html>
```